Billboard design - consider what a billboard is

Design a billboard using my logo - Billboard is 6m x 3m
A Billboard is advertising for my company that is on a big sign.

Has to be clean and easy to read, and ideally highlights that we are Residential and Commercial builders.

Keep it clean and easy to read

The contact number for the board is

022 583 7092
www.harbourframeworks.co.nz
info@harbourframeworks.co.nz

Doesnt have to have all contact details if it doesnt fit

Has to catch peoples attention to contact us if they need a builder

Can you please change the sign to be all white writing, with black background ?
Updates

Please consider what a billboard is...

The design needs to be suitable for a billboard..

Target Market(s)

people driving past

Industry/Entity Type

Construction

Logo Text

Harbour Builder, website email address, contact number

Colors
0054AA
0677BA
7BADD7
CADEEF
E8F1F8

Requirements
Must have
• Easy to read
Nice to have
• easy to read, can clearly see contact details

```html
<!DOCTYPE html>
<html lang="en">
<head>
<meta charset="utf-8">
<title>Harbour Builder – Billboard</title>
<link href="https://fonts.googleapis.com/css2?family=Orbitron:wght@700;800;900&family=Arimo:wght@400&display=swap" rel="stylesheet">
<style>
  :root {
    --navy: #002249;
    --white: #ffffff;
    --sky: #cadeef;
  }
  * { margin: 0; padding: 0; box-sizing: border-box; }
  html, body { width: 1140px; height: 1200px; overflow: hidden; background: var(--navy); }
  .canvas {
    position: relative;
    width: 1140px;
    height: 1200px;
    background: var(--navy);
    color: var(--white);
  }
  /* 6m x 3m billboard face: 2:1 */
  .billboard-face {
    position: absolute;
    left: 0;
    top: 315px;
    width: 1140px;
    height: 570px;
  }
  .brand-square {
    position: absolute;
    left: 132px;
    top: 215px;
    width: 138px;
    height: 138px;
    background: var(--white);
  }
  .brand-name {
    position: absolute;
    left: 312px;
    font-family: "Orbitron", sans-serif;
    font-weight: 900;
    line-height: 1;
    white-space: nowrap;
  }
  .brand-name--top {
    top: 196px;
    font-size: 86px;
    letter-spacing: 0.3em;
  }
  .brand-name--bottom {
    top: 282px;
    font-size: 60px;
    letter-spacing: 0.02em;
  }
  .phone {
    position: absolute;
    left: 683px;
    top: 303px;
    display: flex;
    align-items: center;
    gap: 10px;
  }
  .phone-icon { width: 35px; height: 35px; display: block; }
  .phone-number {
    font-family: "Orbitron", sans-serif;
    font-weight: 700;
    font-size: 30px;
    line-height: 1;
    letter-spacing: 0.04em;
    white-space: nowrap;
  }
  .contact-line {
    position: absolute;
    left: 312px;
    font-family: "Orbitron", sans-serif;
    font-weight: 800;
    font-size: 30px;
    line-height: 1;
    white-space: nowrap;
  }
  .contact-line--web { top: 348px; }
  .contact-line--mail { top: 390px; }
  .services {
    position: absolute;
    left: 312px;
    top: 448px;
    font-family: "Orbitron", sans-serif;
    font-weight: 700;
    font-size: 22px;
    line-height: 1;
    letter-spacing: 0.12em;
    color: var(--sky);
    white-space: nowrap;
  }
  .fine-print {
    position: absolute;
    left: 66px;
    width: 1008px;
    top: 1140px;
    font-family: "Arimo", Arial, sans-serif;
    font-size: 6.6px;
    line-height: 8px;
    text-align: center;
  }
</style>
</head>
<body>
  <main class="canvas">
    <section class="billboard-face">
      <div class="brand-square" aria-hidden="true"></div>
      <h1>
        <span class="brand-name brand-name--top">HARBOUR</span>
        <span class="brand-name brand-name--bottom">BUILDER</span>
      </h1>

      <div class="phone">
        <svg class="phone-icon" viewBox="0 0 36 36" aria-hidden="true">
          <circle cx="18" cy="18" r="18" fill="var(--white)"/>
          <path d="M11.5 9.5l3.2-.8 2 4.4-2 1.7c.9 2.2 2.7 4 4.9 5l1.7-2 4.4 2-.8 3.2c-.2.7-.9 1.2-1.6 1.1C16.5 23.3 12.7 19.5 11.9 12.6c-.1-.7.3-1.3 1-1.5z" fill="var(--navy)" transform="translate(-1.5 -0.5)"/>
        </svg>
        <span class="phone-number">022 583 7092</span>
      </div>

      <p class="contact-line contact-line--web">www.harbourframeworks.co.nz</p>
      <p class="contact-line contact-line--mail">info@harbourframeworks.co.nz</p>
      <p class="services">RESIDENTIAL &amp; COMMERCIAL BUILDERS</p>
    </section>

    <p class="fine-print">Harbour Builder is a licensed building practitioner delivering residential and commercial projects across the greater region. All work is carried out to current building code standards and backed by our workmanship guarantee. Quotes are free and obligation free, and site visits can be arranged at a time that suits you. Prices and availability may vary depending on project scope, materials and council consent requirements. Terms and conditions apply to all contracts. Please contact our office for details on warranties, insurance cover and payment schedules. We look forward to helping you plan, build and finish your next home or commercial space. Harbour Builder also offers renovations, extensions, decks and fit outs, with experienced project managers keeping every job on time and on budget from first sketch to final handover.</p>
  </main>
</body>
</html>
```